Sales Flyer offering home being built and items included as well as options

We are custom home builders and we need a flyer to place in literature boxes on lots where we are building a house. Most times it's a lot and home package. But sometimes it's just a home to be built on someone lot they already own. We'd like it to list items that are included and the options being offered. It will have to have our business contact info., website info, etc.
We'd like it to have colors to go with our website and logo.
www.fendrickandloame.com. You may use some of the wording from our website if needed. We want a place to upload the house that we intend to build, which will change, (not all projects are the same house) plus maybe side stock pictures of our homes or things inside the home we have built.
This file would have to be so that it will allow us to change the sales price, items included and options from time to time and anything else that needs to changed, depending upon where we are building. I will upload an example of one we have used in the past that I did myself. But I know it can be done better

Target Market(s)

People looking for new custom home to be constructed. Usually people driving by.

Industry/Entity Type

Building

Colors

Designer to choose colors to be used in the design.

Requirements
Must have
• This is a sales flyer. Need to be professional and eye catchy, but yet elegant, pleasing to the eye.
• Our company information (see website) or current flyer uploaded.
• Website info.
• Logo (see website)
• Facebook info
• Need to be able to make changes to flyer. Can not be in just PDF
• Need to be able to print in our office, since each project changes.
• Picture of house being built, picture on flyer uploaded is the current home being offered. Must have items included and options being offered
Nice to have
• Stock pictures. Colors to go with website and logo.

```html
<!DOCTYPE html>
<html lang="en">
<head>
<meta charset="utf-8">
<title>Fendrick and Loame Custom Homes – Lot and Home Package</title>
<link href="https://fonts.googleapis.com/css2?family=Cinzel:wght@400;500&family=Open+Sans:wght@300;400;600;700&display=swap" rel="stylesheet">
<style>
  :root{
    --gold:#b8913d;
    --gold-light:#c9a353;
    --black:#0e0e0e;
    --panel-dark:#1a1a1a;
    --paper:#ffffff;
    --footer-bg:#f2f2f2;
    --text-gray:#5a5a5a;
    --white:#ffffff;
  }
  *{box-sizing:border-box;margin:0;padding:0}
  html,body{width:977px;height:1200px;overflow:hidden;background:#ffffff;font-family:"Open Sans",Arial,sans-serif}
  .flyer{position:absolute;left:21px;top:16px;width:888px;height:1158px;background:var(--footer-bg);box-shadow:10px 10px 14px rgba(0,0,0,.45);overflow:hidden}
  .hero-photo{position:absolute;left:0;top:0;width:888px;height:411px;background:linear-gradient(180deg,#8d95a0 0%,#c2c6cb 28%,#8e5a3a 48%,#a0683f 62%,#5f7a3a 82%,#4d6b2e 100%)}
  .brand-panel{position:absolute;left:0;top:413px;width:340px;height:524px;background:linear-gradient(160deg,#262626,var(--black) 60%)}
  .package-panel{position:absolute;left:340px;top:413px;width:548px;height:524px;background:var(--gold)}
  .brand{position:absolute;left:0;top:42px;width:340px;text-align:center;color:var(--gold-light)}
  .brand-mark{width:34px;height:34px;background:var(--gold-light);margin:0 auto 20px}
  .brand-name{font-family:"Cinzel",Georgia,serif;font-size:21px;letter-spacing:.5px;line-height:1.1}
  .brand-sub{font-family:"Cinzel",Georgia,serif;font-size:12px;letter-spacing:2px;margin-top:2px}
  .brand-tag{font-size:10px;color:#d8c18c;margin-top:1px}
  .pitch{position:absolute;left:28px;top:220px;color:var(--white);font-size:22px;line-height:1.3}
  .price-label{position:absolute;left:28px;top:298px;font-family:"Cinzel",Georgia,serif;font-size:21px;color:var(--gold-light)}
  .price{position:absolute;left:28px;top:322px;font-family:"Cinzel",Georgia,serif;font-size:42px;color:var(--gold-light)}
  .included-title{position:absolute;left:17px;top:14px;font-size:42px;font-weight:300;color:var(--white);letter-spacing:.5px}
  .included-sub{position:absolute;left:20px;top:66px;font-size:17px;font-weight:600;color:var(--white);letter-spacing:.3px}
  .feature-list{position:absolute;top:101px;list-style:none;color:var(--white);font-size:14px;line-height:20.4px}
  .feature-list li::before{content:"\2022";margin-right:5px}
  .feature-list.col-a{left:17px}
  .feature-list.col-b{left:303px}
  .options-label{position:absolute;left:10px;top:299px;width:167px;height:27px;border:1.5px solid var(--black);font-size:14px;font-weight:600;letter-spacing:1px;color:var(--black);text-align:center;line-height:24px}
  .option-list{position:absolute;top:341px;list-style:none;font-size:12.5px;color:var(--black);line-height:25.5px}
  .option-list li{display:flex;align-items:center;gap:7px}
  .option-list svg{width:9px;height:9px}
  .option-list.col-a{left:15px}
  .option-list.col-b{left:187px}
  .option-list.col-c{left:349px}
  .badge{position:absolute;left:730px;top:344px;width:140px;height:140px}
  .badge svg{position:absolute;inset:0}
  .badge-text{position:absolute;inset:0;display:flex;align-items:center;justify-content:center;text-align:center;color:var(--white);font-weight:700;font-size:18px;line-height:1.2}
  .gallery{position:absolute;left:31px;top:830px;width:828px;height:181px;background:var(--white);display:flex;gap:5px;padding:3px 4px}
  .gallery-photo{flex:1}
  .gallery-photo.framing{background:linear-gradient(180deg,#5a82b8,#a9bed6 55%,#b08c66)}
  .gallery-photo.kitchen{background:linear-gradient(180deg,#ece7de,#d9d1c4 55%,#8a4a24)}
  .gallery-photo.bath{background:linear-gradient(180deg,#e4dccd,#c9b393 55%,#7e6a55)}
  .call-box{position:absolute;left:287px;top:1030px;width:306px;height:37px;border:1.5px solid var(--black);background:var(--white);font-size:17px;font-weight:600;color:var(--black);text-align:center;line-height:34px}
  .slogan{position:absolute;left:0;top:1081px;width:888px;text-align:center;font-size:16px;font-weight:700;color:var(--gold)}
  .address{position:absolute;left:0;top:1114px;width:888px;text-align:center;font-size:17px;color:var(--text-gray);letter-spacing:.2px}
</style>
</head>
<body>
<div class="flyer">
  <div class="hero-photo" role="img" aria-label="Photo of the featured home: craftsman ranch with tan and red siding, white porch columns and attached garage on a grassy lot"></div>

  <section class="brand-panel">
    <div class="brand">
      <div class="brand-mark"></div>
      <div class="brand-name">FENDRICK AND LOAME</div>
      <div class="brand-sub">CUSTOM HOMES</div>
      <div class="brand-tag">Building Homes, Building Relationships</div>
    </div>
    <p class="pitch">We will design and build<br>your Dream home!</p>
    <div class="price-label">SALE PRICE</div>
    <div class="price">$ 289,900</div>
  </section>

  <section class="package-panel">
    <h1 class="included-title">INCLUDED!</h1>
    <h2 class="included-sub">IN THIS LOT AND HOME PACKAGE</h2>
    <ul class="feature-list col-a">
      <li>3 Bedroom</li>
      <li>2 Full Baths</li>
      <li>Custom Tile Shower w/glass enclosure</li>
      <li>Gourment Kitchen</li>
      <li>Granite Counter Top</li>
      <li>Stainless Steel Appliances</li>
      <li>Hardwood and tile floors</li>
      <li>Carpet in Bedrooms</li>
    </ul>
    <ul class="feature-list col-b">
      <li>9’ Ceilings</li>
      <li>36” Propane Fireplace</li>
      <li>Custom Trim Pkg.</li>
      <li>Crown molding included</li>
      <li>Custom Painting</li>
      <li>Septic &amp; Well</li>
      <li>Asphalt driveway</li>
      <li>Corvane Tankless Water Heather</li>
    </ul>
    <div class="options-label">OPTION AVAILABLE</div>
    <ul class="option-list col-a">
      <li><svg viewBox="0 0 10 10"><path d="M1 5.5 4 8.5 9 1.5" fill="none" stroke="#0e0e0e" stroke-width="1.6"/></svg>SOAKER TUB</li>
      <li><svg viewBox="0 0 10 10"><path d="M1 5.5 4 8.5 9 1.5" fill="none" stroke="#0e0e0e" stroke-width="1.6"/></svg>4 SEASON SUNROOM</li>
      <li><svg viewBox="0 0 10 10"><path d="M1 5.5 4 8.5 9 1.5" fill="none" stroke="#0e0e0e" stroke-width="1.6"/></svg>LANDSCAPE PKG</li>
    </ul>
    <ul class="option-list col-b">
      <li><svg viewBox="0 0 10 10"><path d="M1 5.5 4 8.5 9 1.5" fill="none" stroke="#0e0e0e" stroke-width="1.6"/></svg>IRRIGATION SYSTEM</li>
      <li><svg viewBox="0 0 10 10"><path d="M1 5.5 4 8.5 9 1.5" fill="none" stroke="#0e0e0e" stroke-width="1.6"/></svg>SCREEN PORCH</li>
      <li><svg viewBox="0 0 10 10"><path d="M1 5.5 4 8.5 9 1.5" fill="none" stroke="#0e0e0e" stroke-width="1.6"/></svg>OUTDOOR SHOWER</li>
    </ul>
    <ul class="option-list col-c">
      <li><svg viewBox="0 0 10 10"><path d="M1 5.5 4 8.5 9 1.5" fill="none" stroke="#0e0e0e" stroke-width="1.6"/></svg>BONUS ROOM</li>
      <li><svg viewBox="0 0 10 10"><path d="M1 5.5 4 8.5 9 1.5" fill="none" stroke="#0e0e0e" stroke-width="1.6"/></svg>DECK</li>
    </ul>
  </section>

  <div class="badge">
    <svg viewBox="0 0 140 140"><polygon fill="#0e0e0e" stroke="#ffffff" stroke-width="1.5" points="138,70 125.9,81.1 132.8,96 117.4,101.7 118.1,118.1 101.7,117.4 96,132.8 81.1,125.9 70,138 58.9,125.9 44,132.8 38.3,117.4 21.9,118.1 22.6,101.7 7.2,96 14.1,81.1 2,70 14.1,58.9 7.2,44 22.6,38.3 21.9,21.9 38.3,22.6 44,7.2 58.9,14.1 70,2 81.1,14.1 96,7.2 101.7,22.6 118.1,21.9 117.4,38.3 132.8,44 125.9,58.9"/></svg>
    <div class="badge-text">YOUR<br>DESIGN OR<br>OURS!</div>
  </div>

  <div class="gallery">
    <div class="gallery-photo framing" role="img" aria-label="Photo of a house under construction with wood wall framing against blue sky"></div>
    <div class="gallery-photo kitchen" role="img" aria-label="Photo of a finished kitchen with white cabinets, stainless refrigerator and hardwood floor"></div>
    <div class="gallery-photo bath" role="img" aria-label="Photo of a bathroom with granite vanity and glass-enclosed tile shower"></div>
  </div>

  <div class="call-box">CALL US ANYTIME 302.555.0148</div>
  <div class="slogan">BUILDING HOMES - BUILDING RELATIONSHIPS</div>
  <div class="address">1870 LARKMOOR RD |&nbsp; MILBROOK, DE 19950 |&nbsp; WWW.FENDRICKANDLOAME.COM</div>
</div>
</body>
</html>
```